Larkwell Answering Service Brochure

Design a brochure for an answering service/call center based on the information submitted/attached. Photos and text will be included. Would like it designed to complement the logo provided. This brochure will explain to the potential customer who we are and what we have to offer.

The Larkwell representatives take and processes inbound calls, 24-7-365

Target Market(s)

Any business, however, primarily Medical, oil and gas, non profits, and the service industry

Industry/Entity Type

Telecommunications

Font styles to use
Serif
Other font styles liked:
• coordinate with logo

Requirements
Must have
• Modern, bright, bold and neatly structured brochure that will complement the logo and our brand.

```html
<!DOCTYPE html>
<html lang="en">
<head>
<meta charset="utf-8">
<title>Larkwell Answering Service Brochure</title>
<link href="https://fonts.googleapis.com/css2?family=Open+Sans:wght@400;700&family=Saira+Condensed:wght@600&family=Great+Vibes&display=swap" rel="stylesheet">
<style>
  :root{
    --page-bg:#c2beba;
    --paper:#ffffff;
    --charcoal:#302c2e;
    --red:#d8232a;
    --heading-red:#e8505b;
    --body:#3d3a3b;
    --subhead:#4a4749;
  }
  *{box-sizing:border-box;margin:0;padding:0}
  html,body{width:1200px;height:1200px;overflow:hidden;background:var(--page-bg)}
  body{font-family:"Open Sans",Arial,sans-serif;color:var(--body)}
  .brochure{position:absolute;left:30px;top:160px;width:1140px;height:880px;background:var(--paper);display:flex;box-shadow:0 20px 40px rgba(0,0,0,.18);overflow:hidden}
  .panel{position:relative;width:380px;height:100%;padding:0 34px}
  .panel + .panel{border-left:1px solid #e6e3e3}
  .waves{position:absolute;inset:0;width:1140px;height:880px;pointer-events:none;z-index:3}
  .photo{position:absolute}
  .photo--agent-desk{left:0;top:0;width:380px;height:230px;background:linear-gradient(120deg,#efe7e4 0%,#d9c4bc 40%,#b99a8d 55%,#e9e6e6 100%)}
  .photo--agent-headset{left:0;top:430px;width:380px;height:450px;background:radial-gradient(ellipse at 55% 40%,#e8cfc3 0%,#d7c8c2 30%,#eef0f2 65%,#ffffff 100%)}
  p{font-size:12.5px;line-height:1.45;margin-bottom:14px}
  .section-title{font-family:"Saira Condensed",Arial Narrow,sans-serif;font-weight:600;font-variant:small-caps;color:var(--heading-red);font-size:30px;line-height:1.05;margin:10px 0 14px}
  .service-title{font-weight:700;color:var(--subhead);font-size:17px;margin:18px 0 8px}
  .service-list{list-style:none;font-size:12.5px;line-height:1.45;margin-bottom:14px}
  .service-list li::before{content:"•";display:inline-block;width:22px}
  .panel--intro .intro-copy{margin-top:250px;padding-right:100px}
  .years-badge{position:absolute;left:272px;top:236px;width:96px;height:96px;border-radius:50%;background:var(--red);color:#fff;font-family:"Great Vibes",cursive;text-align:center;display:flex;flex-direction:column;justify-content:center;line-height:.9}
  .years-badge .num{font-size:36px}
  .years-badge .word{font-size:24px}
  .intro-copy-full{padding-right:0}
  .panel--services{padding-top:80px}
  .panel--automated{padding-top:98px}
</style>
</head>
<body>
<main class="brochure">
  <section class="panel panel--intro">
    <div class="photo photo--agent-desk" role="img" aria-label="Photo of a smiling call centre agent wearing a headset at her desk"></div>
    <div class="years-badge"><span class="num">84</span><span class="word">years</span></div>
    <div class="intro-copy">
      <p>Larkwell, over the past 84 years, has operated through wars, floods and hurricanes. Our long history is important as it shows Consistency, Professionalism, Experience, and a Can Do Attitude, which is hard to find in the answering service industry today.</p>
    </div>
    <p>At Larkwell, you'll never be just another a number. We will become part of YOUR team on day one and remain there, ready and honored to serve by providing reliable, professional answering services, 24-7-365, as needed.</p>
    <p>Larkwell Answering Service is your award winning, five start center, backed by critical redundancy and a solid infrastructure, for the highest availability possible.</p>
    <h2 class="section-title">Automated or Live –<br>Answering Services That<br>Work For You</h2>
    <p>Tell us about your needs and your budget and we'll do the rest. Larkwell selects a system that satisfies your basic requirements, then evaluates your business to find a long-term solution that will work for you and your customers.</p>
  </section>

  <section class="panel panel--services">
    <h2 class="section-title">Still<br>Growing? Find a<br>Scalable Phone Answering<br>Service</h2>
    <p>A scalable solution is one that doesn't waste resources when you don't need them, but easily adapts to future growth. All of our services at Larkwell grow with you, meaning you don't pay for additional support until you need it.</p>
    <h3 class="service-title">Live Answering Service</h3>
    <p>Brightline Response is more than an answering service, it's an extension of your company. Our professional representatives take pride in being your direct line of communication with existing customers, potential customers and valued business partners. Before we start fielding calls, our representatives are trained according to the details of your business and industry.</p>
    <ul class="service-list">
      <li>24 Hour Answering Service</li>
      <li>Virtual Receptionist / Virtual Assistant</li>
      <li>Live Message Relay</li>
      <li>Help Desk Overflow</li>
      <li>Call Screening</li>
      <li>Bilingual Answering (Spanish Answering Service)</li>
      <li>Automated Services</li>
    </ul>
    <h3 class="service-title">Automated Services</h3>
    <p>Live answering services are not necessary for all businesses. Brightline Response offers automated answering services as a cost-effective option for continuous cus-</p>
  </section>

  <section class="panel panel--automated">
    <p>tomer contact. And just because it's "automated" that doesn't mean it isn't tailored to the specific needs of your business.</p>
    <p>(Live and automated services can be combined for a very cost effective and professional solution.)</p>
    <p>Here are some of the customizable automated solutions we offer for businesses of all sizes:</p>
    <ul class="service-list">
      <li>Voice Mail (with or without extensions/sub-boxes)</li>
      <li>Voice Mail with Operator Revert</li>
    </ul>
    <div class="photo photo--agent-headset" role="img" aria-label="Photo of a smiling customer service representative wearing a headset"></div>
  </section>

  <svg class="waves" viewBox="0 0 1140 880" aria-hidden="true">
    <path d="M380,0 H1140 V60 C960,26 700,22 380,34 Z" fill="var(--charcoal)"/>
    <path d="M380,34 C700,22 960,26 1140,60 V74 C960,40 700,34 380,42 Z" fill="var(--red)"/>
    <path d="M0,880 C170,800 470,782 760,790 V880 Z" fill="var(--charcoal)"/>
    <path d="M0,866 C170,786 470,766 760,774 V790 C470,782 170,800 0,880 Z" fill="var(--red)"/>
  </svg>
</main>
</body>
</html>
```